Tour Company Needs Poster for Box Office

We need a poster to promote walking tours in Aspen, Colorado. It should be attention grabbing with a vintage look similar to old west shows or circus promotions. It needs to promote "Birchvale Strolling Outings" 3 different tours (an evening ghost tour "Birchvale's NightVeil", a classic historic tour "Birchvale's Then and Now" & a sightseeing tour "Beyond the Quiet Lane"). Attached images should be used in conjunction with the different tour promotions. Poster should be full color and the size needs to be 24" wide X 36 " high.

Requirements
Must have
• Individual tour tag lines
Birchvale's NightVeil "Ghosts Murder & Mayhem"
Birchvale's Then and Now" Classic Historical Tour"
Beyond the Quiet Lane "Historic West End to the River"

Company Logo can be small towards the bottom of the poster and paired with the quote "Like Pellow he Loves Spinning Tales! -Kelbrook's Journeys"

website should be included www.BirchvaleStrollingOutings.example
Nice to have
• Small Quotes to include
"theatrics, humor, wit and dazzling manner"
"awesome story teller"
"should not be missed"

```html
<!DOCTYPE html>
<html lang="en">
<head>
<meta charset="utf-8">
<title>Birchvale Strolling Outings – Tour Poster</title>
<link rel="stylesheet" href="https://fonts.googleapis.com/css2?family=Bowlby+One&family=Bangers&family=Archivo+Black&family=Caveat:wght@700&display=swap">
<style>
  :root {
    --paper: #f6efdc;
    --ink: #3d3a2c;
    --yellow: #f5e84a;
    --red: #ef4f37;
    --green: #3fae49;
    --blue: #2aa7d8;
    --cream: #fbf3d8;
    --white: #ffffff;
    --photo-dark: #4a463d;
    --photo-sky: #b9b5ad;
    --photo-land: #6e6658;
  }
  * { margin: 0; padding: 0; box-sizing: border-box; }
  html, body { width: 800px; height: 1200px; overflow: hidden; background: var(--paper); }
  .poster { position: relative; width: 800px; height: 1200px; overflow: hidden; background: var(--paper); color: var(--ink); font-family: "Bowlby One", sans-serif; }
  .abs { position: absolute; }

  /* Header */
  .brand-stack { left: 30px; top: 18px; width: 360px; text-align: center; line-height: 0.95; text-transform: uppercase; }
  .brand-stack .small { font-size: 30px; letter-spacing: 6px; }
  .brand-stack .big { font-size: 46px; }
  .divider { left: 398px; top: 26px; width: 4px; height: 150px; background: var(--ink); }
  .place { left: 412px; top: 18px; width: 372px; text-align: center; line-height: 0.98; text-transform: uppercase; }
  .place .city { font-size: 72px; letter-spacing: 2px; }
  .place .state { font-size: 54px; }
  .presents { left: 412px; top: 190px; width: 372px; text-align: center; font-family: "Archivo Black", sans-serif; font-size: 17px; letter-spacing: 1px; }

  /* Ghost tour band */
  .ghost-band { left: 29px; top: 232px; width: 751px; height: 253px; background: var(--yellow); }
  .ghost-tagline { left: 29px; top: 240px; width: 751px; text-align: center; font-family: "Archivo Black", sans-serif; font-size: 18px; letter-spacing: 0.5px; }
  .ghost-title-box { left: 193px; top: 268px; width: 568px; height: 167px; background: var(--ink); border-radius: 18px; display: flex; flex-direction: column; align-items: center; justify-content: center; }
  .ghost-title { font-family: "Bangers", sans-serif; color: var(--red); font-size: 72px; line-height: 0.95; letter-spacing: 3px; text-align: center; text-transform: uppercase; transform: rotate(-2deg); }

  .photo { background: linear-gradient(180deg, var(--photo-sky), var(--photo-land)); }
  .photo.dark { background: radial-gradient(ellipse at 50% 55%, #8c8678, var(--photo-dark) 70%); }

  /* Historic tour block */
  .history-frame { left: 212px; top: 470px; width: 428px; height: 212px; background: var(--white); border: 3px solid var(--red); }
  .title-box { display: flex; align-items: center; justify-content: center; text-transform: uppercase; color: var(--ink); white-space: nowrap; }
  .then-box { left: 225px; top: 483px; width: 399px; height: 68px; background: var(--green); border: 3px solid var(--red); font-size: 33px; }
  .history-tagline { left: 212px; top: 560px; width: 428px; text-align: center; font-family: "Archivo Black", sans-serif; font-size: 16px; }
  .now-box { left: 225px; top: 588px; width: 377px; height: 64px; background: var(--blue); border: 3px solid var(--red); font-size: 48px; }

  /* Sightseeing tour */
  .pill { display: flex; align-items: center; justify-content: center; border-radius: 50%; font-family: "Bangers", sans-serif; color: var(--cream); letter-spacing: 2px; text-transform: uppercase; background: var(--red); white-space: nowrap; }
  .pill-left { left: 18px; top: 682px; width: 258px; height: 101px; font-size: 42px; border: 6px solid var(--green); box-shadow: inset 0 0 0 4px var(--cream); }
  .pill-right { left: 500px; top: 672px; width: 283px; height: 118px; font-size: 50px; border: 6px solid var(--blue); box-shadow: inset 0 0 0 4px var(--cream); }

  .route-frame { background: var(--white); border: 3px solid var(--red); }
  .route-box { display: flex; flex-direction: column; align-items: center; justify-content: center; line-height: 0.9; }
  .route-box .script { font-family: "Caveat", cursive; font-size: 34px; align-self: flex-start; margin-left: 18px; }
  .route-box .script.right { align-self: flex-end; margin-right: 30px; margin-left: 0; }
  .route-box .big { font-size: 46px; text-transform: uppercase; }
  .west { left: 65px; top: 850px; width: 320px; height: 82px; background: var(--blue); }
  .river { left: 415px; top: 850px; width: 360px; height: 82px; background: var(--green); }

  /* Quotes */
  .quote { display: flex; align-items: center; justify-content: center; font-family: "Archivo Black", sans-serif; font-size: 14px; text-transform: uppercase; white-space: nowrap; border: 3px solid var(--blue); border-radius: 10px; background: var(--paper); padding: 6px; }
  .quote span { display: flex; align-items: center; justify-content: center; width: 100%; height: 100%; }
  .q-yellow span { background: var(--yellow); }
  .q-red span { background: var(--red); }

  /* Footer */
  .company { left: 29px; top: 1090px; width: 200px; display: flex; align-items: center; gap: 8px; font-family: "Archivo Black", sans-serif; font-size: 19px; line-height: 1.05; color: var(--red); }
  .company .dot { flex: 0 0 22px; height: 22px; border-radius: 50%; background: var(--ink); }
  .press-quote { left: 14px; top: 1160px; width: 260px; font-family: "Archivo Black", sans-serif; font-size: 11px; line-height: 1.2; text-transform: uppercase; }
  .info { left: 300px; top: 1110px; width: 490px; text-align: center; font-family: "Caveat", cursive; font-size: 27px; white-space: nowrap; }
  .website { left: 300px; top: 1154px; width: 490px; text-align: center; font-family: "Archivo Black", sans-serif; font-size: 16px; letter-spacing: 0.3px; white-space: nowrap; }

  .star { fill: var(--red); }
  .star.blue { fill: var(--blue); }
</style>
</head>
<body>
<main class="poster">
  <header>
    <div class="abs brand-stack"><div class="small">Birchvale</div><div class="big">Strolling</div><div class="big">Outings</div></div>
    <div class="abs divider"></div>
    <div class="abs place"><div class="city">Aspen.</div><div class="state">Colorado.</div></div>
    <div class="abs presents">PRESENTS</div>
  </header>

  <section class="ghost-tour">
    <div class="abs ghost-band"></div>
    <div class="abs ghost-tagline">GHOSTS, MURDER AND MAYHEM</div>
    <div class="abs photo dark" style="left:29px;top:278px;width:159px;height:207px;" role="img" aria-label="Costumed guides in period dress holding a lantern at night"></div>
    <div class="abs ghost-title-box"><div class="ghost-title">Birchvale's<br>NightVeil</div></div>
  </section>

  <section class="history-tour">
    <div class="abs photo" style="left:14px;top:500px;width:204px;height:180px;" role="img" aria-label="Mountain valley landscape with sagebrush"></div>
    <div class="abs photo" style="left:630px;top:468px;width:153px;height:210px;" role="img" aria-label="Tour guide in western hat and vest standing in a meadow"></div>
    <div class="abs history-frame"></div>
    <div class="abs title-box then-box">Birchvale's Then</div>
    <div class="abs history-tagline">CLASSICAL HISTORICAL TOUR</div>
    <div class="abs title-box now-box">and Now</div>
  </section>

  <section class="sight-tour">
    <div class="abs photo dark" style="left:285px;top:680px;width:222px;height:190px;" role="img" aria-label="Wooden trail signpost pointing to town landmarks"></div>
    <div class="abs pill pill-left">Beyond the</div>
    <div class="abs pill pill-right">Quiet Lane</div>

    <div class="abs route-frame" style="left:58px;top:835px;width:334px;height:120px;"></div>
    <div class="abs route-box west"><span class="script">Historic</span><span class="big">West End</span></div>
    <div class="abs route-frame" style="left:405px;top:835px;width:378px;height:120px;"></div>
    <div class="abs route-box river"><span class="script right">to the</span><span class="big">River</span></div>
  </section>

  <svg class="abs" style="left:0;top:0;" width="800" height="1200" aria-hidden="true">
    <defs><path id="s" d="M0,-10 L2.9,-3.1 10,-3.1 4.3,1.2 6.2,8.1 0,4 -6.2,8.1 -4.3,1.2 -10,-3.1 -2.9,-3.1Z"/></defs>
    <use href="#s" class="star blue" transform="translate(200,492) scale(0.7)"/>
    <use href="#s" class="star" transform="translate(20,698) scale(0.8)"/>
    <use href="#s" class="star" transform="translate(530,800) scale(1.1)"/>
    <use href="#s" class="star" transform="translate(556,818) scale(0.8)"/>
    <use href="#s" class="star" transform="translate(218,826) scale(1)"/>
    <use href="#s" class="star" transform="translate(262,812) scale(1.2)"/>
    <use href="#s" class="star" transform="translate(774,800) scale(0.8)"/>
    <use href="#s" class="star blue" transform="translate(20,950) scale(0.8)"/>
  </svg>

  <section class="quotes">
    <div class="abs quote q-yellow" style="left:14px;top:957px;width:348px;height:58px;"><span>"Should not be missed"</span></div>
    <div class="abs quote q-red" style="left:435px;top:957px;width:348px;height:58px;"><span>"Awesome story teller"</span></div>
    <div class="abs quote q-red" style="left:180px;top:1015px;width:444px;height:58px;"><span>"Theatrics, humor, wit and dazzling manner"</span></div>
  </section>

  <footer>
    <div class="abs company"><span class="dot"></span><span>Birchvale Strolling Outings</span></div>
    <div class="abs press-quote">"Like Pellow he loves spinning tales! -Kelbrook's Journeys"</div>
    <div class="abs info">For more information and to purchase tickets go to</div>
    <div class="abs website">WWW.BIRCHVALESTROLLINGOUTINGS.EXAMPLE</div>
  </footer>
</main>
</body>
</html>
```